Amber Hollow Productions

I need a business card design for a new freelance film production company using or incorporating the logo:
I want the card to be creative, minimal, yet professional. Feel free to use a variety of different shapes and sizes/ textures for the card.

Industry/Entity Type

Film Production

```html
<!DOCTYPE html>
<html lang="en">
<head>
<meta charset="utf-8">
<title>Amber Hollow Productions – Business Card</title>
<link rel="stylesheet" href="https://fonts.googleapis.com/css2?family=Raleway:wght@400&family=Arimo:wght@400&display=swap">
<style>
  :root {
    --kraft-light: #d7ad6c;
    --kraft-mid: #c79a58;
    --kraft-dark: #a97a3e;
    --film-band: #ebe8e2;
    --paper-light: #f1f1ef;
    --paper-shade: #dcdcda;
    --brand-blue: #2e5fae;
    --page-bg: #ffffff;
  }
  html, body {
    margin: 0;
    padding: 0;
    width: 1200px;
    height: 339px;
    overflow: hidden;
    background: var(--page-bg);
  }
  .canvas {
    position: relative;
    width: 1200px;
    height: 339px;
  }
  .card {
    position: absolute;
    top: 0;
    height: 339px;
    overflow: hidden;
  }
  .card--front { left: 0; width: 593px; }
  .card--back { left: 607px; width: 593px; }

  .kraft {
    background:
      radial-gradient(ellipse at 30% 40%, rgba(255,230,180,0.35), transparent 60%),
      radial-gradient(ellipse at 85% 80%, rgba(120,80,30,0.25), transparent 55%),
      linear-gradient(135deg, var(--kraft-light), var(--kraft-mid) 55%, var(--kraft-dark));
  }
  .film-strip {
    position: absolute;
    display: block;
  }
  .film-strip--top { left: 0; top: 14px; }
  .film-strip--bottom { left: 0; top: 295px; }

  .brand-name {
    position: absolute;
    left: 0;
    width: 593px;
    top: 128px;
    text-align: center;
    font-family: "Raleway", sans-serif;
    font-weight: 400;
    color: var(--brand-blue);
    margin: 0;
    line-height: 1;
  }
  .brand-name__main {
    display: block;
    font-size: 42px;
    letter-spacing: 1px;
  }
  .brand-name__sub {
    display: block;
    margin-top: 18px;
    font-size: 17px;
    letter-spacing: 6px;
  }

  .back-kraft {
    position: absolute;
    left: 0;
    top: 0;
    width: 262px;
    height: 339px;
  }
  .film-strip--vertical { left: 261px; top: 0; }
  .back-paper {
    position: absolute;
    left: 288px;
    top: 0;
    width: 305px;
    height: 339px;
    background:
      radial-gradient(ellipse at 50% 50%, var(--paper-light), var(--paper-shade) 120%);
  }
  .address-label {
    position: absolute;
    left: 0;
    width: 305px;
    top: 161px;
    margin: 0;
    text-align: center;
    font-family: "Arimo", sans-serif;
    font-weight: 400;
    font-size: 28px;
    color: var(--brand-blue);
    line-height: 1;
  }
</style>
</head>
<body>
<main class="canvas">
  <section class="card card--front kraft" aria-label="Card front">
    <svg class="film-strip film-strip--top" width="593" height="27" viewBox="0 0 593 27" aria-hidden="true">
      <defs>
        <pattern id="sprockets-h" width="18" height="27" patternUnits="userSpaceOnUse">
          <rect x="4" y="7" width="11" height="13" fill="#c99c5a"/>
        </pattern>
      </defs>
      <rect width="593" height="27" fill="var(--film-band)"/>
      <rect width="593" height="27" fill="url(#sprockets-h)"/>
    </svg>

    <h1 class="brand-name">
      <span class="brand-name__main">AMBER HOLLOW</span>
      <span class="brand-name__sub">PRODUCTIONS</span>
    </h1>

    <svg class="film-strip film-strip--bottom" width="593" height="30" viewBox="0 0 593 30" aria-hidden="true">
      <rect width="593" height="30" fill="var(--film-band)"/>
      <rect width="593" height="30" fill="url(#sprockets-h)" transform="translate(0,2)"/>
    </svg>
  </section>

  <section class="card card--back" aria-label="Card back">
    <div class="back-kraft kraft"></div>
    <svg class="film-strip film-strip--vertical" width="28" height="339" viewBox="0 0 28 339" aria-hidden="true">
      <defs>
        <pattern id="sprockets-v" width="28" height="18" patternUnits="userSpaceOnUse">
          <rect x="8" y="4" width="12" height="11" fill="#c99c5a"/>
        </pattern>
      </defs>
      <rect width="28" height="339" fill="var(--film-band)"/>
      <rect width="28" height="339" fill="url(#sprockets-v)"/>
    </svg>
    <div class="back-paper">
      <p class="address-label">address:</p>
    </div>
  </section>
</main>
</body>
</html>
```